THE BRIGHT KITE SITTER - Temporary, On The Spot , Child Minding and Dog Walking Service

I am THE BRIGHT KITE SITTER. I am available for temporary on-the-spot bookings, for those times when parents need 1 or 2 hours to duck out to the supermarket but they can' t because their baby is taking a nap. Or maybe they have a 1 to 2 hour appointment where they can't take the kids and have no one to look after them. Or they may be they are at a luncheon and have to reluctantly tear themselves away to pick up the kids from school.
This is where I come to the rescue.
I can be hired for a minimum of 1 hour, or a maximum of 2 hours. I will come to them. Daytime and Evening rates apply. Maximum 3 children at one time.
I will entertain the children, do the odd job around the house, make delicious snacks and I can pickup children from school when necessary. I am also available to walk your beloved dog.
The Bright Kite Sitter is like no other nanny you will ever have - fun, reliable, super-tidy , and comes with impeccable references. Your life will become a whole lot easier with me in it!

I'd like a flyer that looks 'classy' as well as eye-catching. I'm 51 years old, but a 'very young' 51 so I'm also looking for a modern flyer.

Target Market(s)

Busy Mums and Dads and Guardians.

Industry/Entity Type

It Service

Requirements
Must have
• Maximum of 3 children at any 1 time.
Should not have
• Nasty pets!

```html
<!DOCTYPE html>
<html lang="en">
<head>
<meta charset="utf-8">
<title>The Bright Kite Sitter – Flyer</title>
<link rel="stylesheet" href="https://fonts.googleapis.com/css2?family=Archivo+Black&family=Oswald:wght@500;600&family=Open+Sans:wght@600;700;800&display=swap">
<style>
  :root {
    --sky-top: #cfe9f7;
    --sky-bottom: #e8f5fb;
    --sun-yellow: #fde99a;
    --sun-deep: #f9d75c;
    --alert-red: #d7262b;
    --ink-navy: #1f3a66;
    --ink-dark: #1b1b1b;
    --cream: #fbf1d6;
    --rose: #f0a3bd;
    --rose-deep: #e0709a;
    --white: #ffffff;
  }
  * { margin: 0; padding: 0; box-sizing: border-box; }
  html, body { width: 849px; height: 1200px; overflow: hidden; }
  body { background: var(--white); }
  .flyer {
    position: relative; width: 849px; height: 1200px; overflow: hidden;
    background: linear-gradient(180deg, var(--sky-top) 0%, var(--sky-bottom) 60%, var(--white) 100%);
    text-align: center;
  }
  .flyer svg.backdrop { position: absolute; inset: 0; }
  .announce { position: absolute; top: 20px; left: 0; right: 0; }
  .announce-kicker {
    font-family: "Archivo Black", sans-serif; color: var(--alert-red);
    font-size: 38px; letter-spacing: 1px; line-height: 1;
  }
  .announce-sub {
    font-family: "Oswald", sans-serif; font-weight: 600; color: var(--alert-red);
    font-size: 21px; letter-spacing: 1px; line-height: 1; margin-top: 8px;
  }
  .brand-title {
    font-family: "Archivo Black", sans-serif; color: var(--ink-dark);
    font-size: 50px; line-height: 1; margin-top: 14px; letter-spacing: 0.5px;
  }
  .abn {
    position: absolute; top: 186px; left: 0; right: 0;
    font-family: "Open Sans", sans-serif; font-weight: 600; font-size: 16px; color: var(--ink-navy);
    letter-spacing: 1px; line-height: 1;
  }
  .audience { position: absolute; top: 218px; left: 40px; right: 40px; }
  .audience-head {
    font-family: "Archivo Black", sans-serif; color: var(--alert-red);
    font-size: 28px; line-height: 1.1;
  }
  .audience-questions {
    list-style: none; margin-top: 4px;
    font-family: "Oswald", sans-serif; font-weight: 600; color: var(--ink-navy);
    font-size: 25px; line-height: 29px; text-transform: uppercase;
  }
  .illustration {
    position: absolute; left: 235px; top: 478px; width: 300px; height: 385px;
    border-radius: 46% 46% 30% 30%;
    background: radial-gradient(ellipse at 50% 40%, #f4c7b0 0%, #e8a28d 35%, #c9546a 70%, rgba(201,84,106,0) 100%);
    opacity: 0.85;
  }
  .services {
    position: absolute; top: 878px; left: 60px; right: 60px;
    font-family: "Open Sans", sans-serif; font-weight: 700; color: var(--ink-navy);
    font-size: 16px; line-height: 21px;
  }
  .services .promise { color: var(--rose-deep); font-weight: 800; font-size: 13px; text-transform: uppercase; }
  .rates {
    position: absolute; top: 1024px; left: 60px; right: 60px;
    font-family: "Open Sans", sans-serif; font-weight: 800; color: var(--white);
    text-transform: uppercase; line-height: 1.3;
  }
  .rates-label { font-size: 14px; letter-spacing: 1px; }
  .rates-main { font-size: 17px; }
  .rates-note { font-size: 13px; }
  .footer-bar {
    position: absolute; left: 0; right: 0; bottom: 0; height: 60px;
    background: var(--sun-yellow);
    display: flex; justify-content: center; align-items: center; gap: 24px;
    font-family: "Archivo Black", sans-serif; color: var(--ink-dark); font-size: 28px;
  }
</style>
</head>
<body>
<main class="flyer">
  <svg class="backdrop" width="849" height="1200" viewBox="0 0 849 1200" aria-hidden="true">
    <defs>
      <linearGradient id="sunband" x1="0" y1="0" x2="0" y2="1">
        <stop offset="0" stop-color="#f9d75c"/>
        <stop offset="1" stop-color="#fde99a"/>
      </linearGradient>
    </defs>
    <path d="M0 0 H849 V160 Q640 185 424 176 Q200 168 0 188 Z" fill="url(#sunband)"/>
    <g fill="#ffffff" opacity="0.7">
      <ellipse cx="90" cy="620" rx="110" ry="34"/>
      <ellipse cx="760" cy="560" rx="120" ry="36"/>
      <ellipse cx="720" cy="760" rx="100" ry="30"/>
      <ellipse cx="130" cy="800" rx="120" ry="32"/>
    </g>
    <path d="M0 872 Q210 852 424 866 Q640 880 849 858 V1020 H0 Z" fill="#fbf1d6"/>
    <path d="M0 1022 Q220 1008 424 1016 Q640 1026 849 1010 V1140 H0 Z" fill="#f0a3bd"/>
  </svg>

  <header class="announce">
    <p class="announce-kicker">SHE HAS ARRIVED!</p>
    <p class="announce-sub">FOR TEMPORARY ON-THE-SPOT BOOKINGS</p>
    <h1 class="brand-title">THE BRIGHT KITE SITTER</h1>
  </header>
  <p class="abn">ABN: 12 345 678 910</p>

  <section class="audience">
    <h2 class="audience-head">BUSY MUMS AND DADS AND GUARDIANS!</h2>
    <ul class="audience-questions">
      <li>Need to go to the supermarket but can't</li>
      <li>because the baby's asleep?</li>
      <li>Have an appointment but you can't go</li>
      <li>because you have the children?</li>
      <li>Reluctantly have to tear yourself away</li>
      <li>from that luncheon because the children</li>
      <li>need to be picked up from school?</li>
    </ul>
  </section>

  <div class="illustration" role="img" aria-label="Illustration of a smiling nanny holding a baby while vacuuming"></div>

  <section class="services">
    <p>The Bright Kite Sitter will come to you!</p>
    <p>She will entertain your children, do the odd job around the house, and make delicious snacks. She will also pickup children from school when necessary and walk your beloved dog.</p>
    <p class="promise">The Bright Kite Sitter is fun, reliable, and comes with impeccable references.</p>
    <p>And she is here to make your life a whole lot easier!</p>
  </section>

  <section class="rates">
    <p class="rates-label">Day rates:</p>
    <p class="rates-main">Minimum hire 1hr - $30.00 &nbsp; Maximum hire 2hrs - $55.00</p>
    <p class="rates-note">Maximum 3 children. Evening rates apply.</p>
    <p class="rates-note">For areas over 10km and up to 20km from Harbourvale, an<br>additional $10 fee applies on the overall hire rate.</p>
  </section>

  <footer class="footer-bar">
    <span class="brand-name">THE BRIGHT KITE SITTER</span>
    <span class="phone">0400 123 987</span>
  </footer>
</main>
</body>
</html>
```